RW dental business card. A family dental practice.

Logo plus the following details.

RW Dental
Dr. Marcus Ellory D.D.S
Family. Implant.Cosmetic

48 Fernbrook Lane, Unit 12-13
Markham, ON K2P7R4

Tel: 905-318-2670
Fx:905-318-9025
rwdental-sample.ca

On the double side:

Next app: ______________________

Please notify us at least 48hours in advance to avoid cancellation fees.

Target Market(s)

Family Dental Services

Industry/Entity Type

Dental

Contact Information for Business Card

Put logo prominently and all the info along with it.

Font styles to use
Other font styles liked:
• See Logo Font

Colors
0255a3
3277b5
85acd3
00a990
33b8a4

Requirements
Must have
• Logo and the info stated above.
• See the logo color scheme.
• Or a grayscale (Black, white gray) combination
Nice to have
• A modern unique layout
Should not have
• too simple a design

```html
<!DOCTYPE html>
<html lang="en">
<head>
<meta charset="utf-8">
<title>RW Dental – Business Card Concepts</title>
<link href="https://fonts.googleapis.com/css2?family=Marcellus&family=Pathway+Gothic+One&family=Cabin+Condensed&display=swap" rel="stylesheet">
<style>
  :root{
    --blue:#0e55a3;
    --blue-mid:#3277b5;
    --teal:#10b09c;
    --teal-light:#33b8a4;
    --ink:#111;
    --paper:#fff;
  }
  *{box-sizing:border-box;margin:0;padding:0}
  html,body{width:1200px;height:1200px;overflow:hidden;background:var(--paper)}
  .sheet{position:relative;width:1200px;height:1200px}
  .card{position:absolute;width:467px;height:267px;border:1.5px solid var(--ink);background:var(--paper);overflow:hidden}
  .card--front-a{left:110px;top:309px}
  .card--back-a{left:622px;top:309px}
  .card--front-b{left:121px;top:623px}
  .card--back-b{left:622px;top:623px}

  .brand{position:absolute;left:0;width:232px;text-align:center}
  .brand__name{top:44px;font-family:"Marcellus",serif;font-weight:400;font-size:30px;line-height:36px;color:var(--blue);letter-spacing:.3px}
  .brand__tagline{top:88px;font-family:"Cabin Condensed",sans-serif;font-size:13px;line-height:16px;color:var(--teal)}

  .name-badge{position:absolute;display:flex;align-items:center;justify-content:center;gap:8px;font-family:"Pathway Gothic One",sans-serif;font-weight:400;white-space:nowrap}
  .name-badge__square{display:block;flex:none}
  .name-badge--front{left:0;width:232px;top:166px;font-size:24px;line-height:28px;color:var(--blue)}
  .name-badge--front .name-badge__square{width:14px;height:14px;background:var(--teal)}
  .name-badge--back{left:0;width:234px;top:112px;font-size:34px;line-height:40px;color:#fff}
  .name-badge--back .name-badge__square{width:20px;height:20px;background:var(--teal)}

  .divider{position:absolute;left:213px;top:34px;width:6px;height:212px}

  .doctor{position:absolute;right:22px;text-align:right;font-weight:400}
  .doctor__name{top:20px;font-family:"Marcellus",serif;font-size:19.5px;line-height:24px;color:var(--blue)}
  .doctor__services{top:48px;font-family:"Pathway Gothic One",sans-serif;font-size:15px;line-height:18px;color:var(--teal)}

  .contact{position:absolute;left:232px;top:158px;list-style:none;font-family:"Pathway Gothic One",sans-serif;font-size:16px;color:var(--teal);line-height:20px}
  .contact li{position:relative;padding-left:26px;white-space:nowrap}
  .contact svg{position:absolute;left:0;top:2px;width:17px;height:17px}

  .back-panel{position:absolute;left:0;top:0;width:234px;height:100%;background:var(--blue)}
  .back-disc{position:absolute;left:-55px;top:-42px;width:302px;height:302px;border-radius:50%;background:var(--blue)}
  .back-ring{position:absolute;left:-60px;top:-55px;width:318px;height:318px;border-radius:50%;border:1.5px solid var(--blue)}
  .back-url{position:absolute;left:0;width:234px;top:218px;text-align:center;font-family:"Pathway Gothic One",sans-serif;font-size:16px;line-height:20px;color:#fff}

  .appointment{position:absolute;left:270px;top:72px;font-family:"Pathway Gothic One",sans-serif;font-size:15px;line-height:18px;color:var(--blue);display:flex;align-items:flex-end}
  .appointment__line{display:inline-block;width:106px;border-bottom:1.5px solid var(--blue);margin-left:3px;margin-bottom:4px}
  .notice{position:absolute;left:270px;width:154px;top:113px;text-align:center;font-family:"Pathway Gothic One",sans-serif;font-size:16px;line-height:20px;color:var(--teal)}
</style>
</head>
<body>
<main class="sheet">

  <section class="card card--front-a">
    <h1 class="brand brand__name">RW Dental</h1>
    <p class="brand brand__tagline">Your dental health support Team</p>
    <p class="name-badge name-badge--front"><span class="name-badge__square"></span>RW Dental</p>
    <svg class="divider" viewBox="0 0 6 212" preserveAspectRatio="none"><ellipse cx="3" cy="106" rx="1.6" ry="106" fill="var(--teal)"/></svg>
    <h2 class="doctor doctor__name">Dr. Marcus Ellory D.D.S</h2>
    <p class="doctor doctor__services">Family. Implant.Cosmetic</p>
    <ul class="contact">
      <li><svg viewBox="0 0 17 17"><rect width="17" height="17" rx="3" fill="var(--blue)"/><path d="M8.5 3.5a3 3 0 0 0-3 3c0 2.2 3 6 3 6s3-3.8 3-6a3 3 0 0 0-3-3z" fill="#fff"/><circle cx="8.5" cy="6.5" r="1.1" fill="var(--blue)"/></svg>48 Fernbrook Lane, Unit 12-13</li>
      <li>Markham, ON K2P7R4</li>
      <li><svg viewBox="0 0 17 17"><rect width="17" height="17" rx="3" fill="var(--blue)"/><rect x="4.5" y="4" width="8" height="9" rx="1" fill="none" stroke="#fff" stroke-width="1.2"/><path d="M6 7h5M6 9.5h5" stroke="#fff"/></svg>905-318-9025</li>
      <li><svg viewBox="0 0 17 17"><rect width="17" height="17" rx="3" fill="var(--blue)"/><path d="M5.5 4.5c1 0 1.5 2 1 2.6l-.7.6c.6 1.4 1.6 2.4 3 3l.6-.7c.6-.5 2.6 0 2.6 1 0 1-1 1.8-2 1.6-3-.6-5.5-3.1-6.1-6.1-.2-1 .6-2 1.6-2z" fill="#fff"/></svg>905-318-2670</li>
    </ul>
  </section>

  <section class="card card--back-a">
    <div class="back-panel"></div>
    <p class="name-badge name-badge--back"><span class="name-badge__square"></span>RW Dental</p>
    <p class="back-url">rwdental-sample.ca</p>
    <p class="appointment">Next app:<span class="appointment__line"></span></p>
    <p class="notice">Please notify us<br>at least 48hours<br>in advance to avoid<br>cancellation fees.</p>
  </section>

  <section class="card card--front-b">
    <h1 class="brand brand__name">RW Dental</h1>
    <p class="brand brand__tagline">Your dental health support Team</p>
    <p class="name-badge name-badge--front"><span class="name-badge__square"></span>RW Dental</p>
    <svg class="divider" viewBox="0 0 6 212" preserveAspectRatio="none"><ellipse cx="3" cy="106" rx="1.6" ry="106" fill="var(--teal)"/></svg>
    <h2 class="doctor doctor__name">Dr. Marcus Ellory D.D.S</h2>
    <p class="doctor doctor__services">Family. Implant.Cosmetic</p>
    <ul class="contact">
      <li><svg viewBox="0 0 17 17"><path d="M8.5 1.5a4.5 4.5 0 0 0-4.5 4.5c0 3.3 4.5 9 4.5 9s4.5-5.7 4.5-9a4.5 4.5 0 0 0-4.5-4.5z" fill="none" stroke="var(--blue)" stroke-width="1.6"/><circle cx="8.5" cy="6" r="1.6" fill="var(--teal)"/></svg>48 Fernbrook Lane, Unit 12-13</li>
      <li>Markham, ON K2P7R4</li>
      <li><svg viewBox="0 0 17 17"><rect x="4" y="2" width="9" height="12" rx="1.5" fill="none" stroke="var(--blue)" stroke-width="1.6"/><path d="M6 6h5M6 9h5" stroke="var(--teal)" stroke-width="1.4"/></svg>905-318-9025</li>
      <li><svg viewBox="0 0 17 17"><path d="M4.5 2.5c1.4 0 2 2.8 1.4 3.6l-1 .8c.8 2 2.2 3.4 4.2 4.2l.8-1c.8-.6 3.6 0 3.6 1.4 0 1.4-1.4 2.5-2.8 2.2-4.2-.8-7.6-4.2-8.4-8.4-.3-1.4.8-2.8 2.2-2.8z" fill="none" stroke="var(--blue)" stroke-width="1.5"/></svg>905-318-2670</li>
    </ul>
  </section>

  <section class="card card--back-b">
    <div class="back-ring"></div>
    <div class="back-disc"></div>
    <p class="name-badge name-badge--back"><span class="name-badge__square"></span>RW Dental</p>
    <p class="back-url">rwdental-sample.ca</p>
    <p class="appointment">Next app:<span class="appointment__line"></span></p>
    <p class="notice">Please notify us<br>at least 48hours<br>in advance to avoid<br>cancellation fees.</p>
  </section>

</main>
</body>
</html>
```